Business Card Design

We need a business card design for a new company called Riverbend Advisory, LLC. We are a project management and software engineering consulting company. We prefer to use blues but am open to any colors. We would like out design to show strength and creativity.
Updates

I've uploaded new logo designs to the project.  Please use these logo designs for the business card. Thanks!

Industry/Entity Type

Software

Contact Information for Business Card

Harold Whitcombe
Consultant
Owner

Riverbend Advisory, LLC

2750 5th Ave. S #3274
Arlington, VA 22917

703-555-0186
hwhitcombe@rvbdax.example
www.rvbdax.example

```html
<!DOCTYPE html>
<html lang="en">
<head>
<meta charset="utf-8">
<title>Riverbend Advisory – Business Card</title>
<link rel="stylesheet" href="https://fonts.googleapis.com/css2?family=Michroma&family=Exo+2:wght@400;500;600&display=swap">
<style>
  :root {
    --navy: #0d3a5e;
    --white: #ffffff;
    --ink: #3a3d42;
    --ink-soft: #6a6e74;
    --stage: #ecedef;
  }
  * { box-sizing: border-box; margin: 0; padding: 0; }
  html, body {
    width: 1200px; height: 906px; overflow: hidden;
    background: var(--stage);
    font-family: "Exo 2", sans-serif;
  }
  .canvas { position: relative; width: 1200px; height: 906px; }
  .card {
    position: absolute; left: 250px; width: 700px; height: 400px;
    overflow: hidden; background: var(--white);
    box-shadow: 0 6px 18px rgba(0,0,0,.18);
  }
  .card--front { top: 40px; }
  .card--back { top: 466px; }

  /* Brand name */
  .brand {
    display: flex; align-items: center; gap: 16px;
    font-family: "Michroma", sans-serif; letter-spacing: 2px;
    text-transform: uppercase; white-space: nowrap;
  }
  .brand__mark { flex: none; width: 22px; height: 22px; }
  .brand--light { color: var(--white); font-size: 30px; }
  .brand--light .brand__mark { background: var(--white); }
  .brand--dark { color: var(--navy); font-size: 14px; letter-spacing: .5px; gap: 10px; }
  .brand--dark .brand__mark { background: var(--navy); width: 12px; height: 12px; }

  /* Front */
  .front__band {
    position: absolute; left: 0; top: 0; width: 100%; height: 232px;
    background: var(--navy);
    display: flex; align-items: center; justify-content: center;
  }
  .front__website {
    position: absolute; left: 56px; bottom: 44px;
    font-size: 20px; font-weight: 500; color: var(--ink); letter-spacing: .5px;
  }

  /* Back */
  .back__top {
    position: absolute; left: 0; top: 0; width: 100%; height: 222px;
    background: linear-gradient(90deg, #d9dadc 0%, #f4f4f5 55%, #e0e1e3 100%);
  }
  .back__logo-box {
    position: absolute; left: 28px; top: 80px; width: 300px; height: 116px;
    background: var(--white);
    display: flex; align-items: center; justify-content: center;
  }
  .holder { position: absolute; right: 48px; top: 44px; text-align: right; }
  .holder__name {
    font-family: "Michroma", sans-serif; font-size: 21px;
    color: var(--ink); letter-spacing: 1px; text-transform: uppercase;
  }
  .holder__title {
    margin-top: 6px; font-size: 13px; font-weight: 500;
    color: var(--ink-soft); letter-spacing: 1.5px; text-transform: uppercase;
  }
  .back__band {
    position: absolute; left: 0; bottom: 0; width: 100%; height: 178px;
    background: var(--navy);
    display: flex; justify-content: space-around; align-items: flex-start;
    padding: 30px 24px 0;
  }
  .contact {
    display: flex; flex-direction: column; align-items: center;
    color: var(--white); font-size: 14px; line-height: 1.4; text-align: center;
    letter-spacing: .5px; white-space: nowrap;
  }
  .contact__icon {
    width: 42px; height: 42px; border-radius: 50%; background: var(--white);
    display: flex; align-items: center; justify-content: center; margin-bottom: 14px;
  }
  .contact__icon svg { width: 24px; height: 24px; }
</style>
</head>
<body>
<main class="canvas">

  <section class="card card--front" aria-label="Business card front">
    <div class="front__band">
      <div class="brand brand--light"><span class="brand__mark"></span>Riverbend Advisory</div>
    </div>
    <p class="front__website">www.rvbdax.example</p>
  </section>

  <section class="card card--back" aria-label="Business card back">
    <div class="back__top">
      <div class="back__logo-box">
        <div class="brand brand--dark"><span class="brand__mark"></span>Riverbend Advisory</div>
      </div>
      <div class="holder">
        <p class="holder__name">Harold Whitcombe</p>
        <p class="holder__title">Consultant / Owner</p>
      </div>
    </div>

    <div class="back__band">
      <div class="contact contact--address">
        <span class="contact__icon">
          <svg viewBox="0 0 24 24" aria-hidden="true"><path d="M3 12 L12 4 L21 12 M6 10 V20 H10 V15 H14 V20 H18 V10" fill="none" stroke="#0d3a5e" stroke-width="2.2" stroke-linejoin="round"/></svg>
        </span>
        <p>2750 5th Ave. S #3274</p>
        <p>Arlington, VA 22917</p>
      </div>
      <div class="contact contact--phone">
        <span class="contact__icon">
          <svg viewBox="0 0 24 24" aria-hidden="true"><path d="M6.6 3.5 L9.5 7.3 L7.8 9.4 C8.9 11.9 11.9 14.9 14.5 16.1 L16.6 14.4 L20.4 17.3 L18.6 20.3 C11 20 4 13 3.7 5.4 Z" fill="#0d3a5e"/></svg>
        </span>
        <p>703-555-0186</p>
      </div>
      <div class="contact contact--web">
        <span class="contact__icon">
          <svg viewBox="0 0 24 24" aria-hidden="true"><g fill="none" stroke="#0d3a5e" stroke-width="1.8"><circle cx="12" cy="12" r="8.5"/><ellipse cx="12" cy="12" rx="3.8" ry="8.5"/><path d="M3.5 12 H20.5 M5 7.5 H19 M5 16.5 H19"/></g></svg>
        </span>
        <p>hwhitcombe@rvbdax.example</p>
        <p>www.rvbdax.example</p>
      </div>
    </div>
  </section>

</main>
</body>
</html>
```